Brindle Yard Care. The best in the biz

I run a lawn care service that offers full service mowing. 100% satisfaction guarantee. Fast, Friendly, quality service "I am your lawns best friend" I cut residential lawns. I offer a mow package that includes trimming, edging and clean up. Prices very from 20 dollars to 75. I want my logo to stand out. Free estimates

Target Market(s)

Home owners

Industry/Entity Type

Landscaping

Contact Information for Business Card

482-615-0273 tomkerl47@quillmail.net Dorian. Brindle Yard care

Colors
f37122
9bcb3c
cadf82

Requirements
Must have
• Company name.
• Phone number
• Email
• My services
• images
Nice to have
• A sun that is growing grass.
Should not have
• Incorrect information

```html
<!DOCTYPE html>
<html lang="en">
<head>
<meta charset="utf-8">
<title>Brindle Yard Care – Business Card</title>
<link href="https://fonts.googleapis.com/css2?family=Open+Sans:wght@400;600&display=swap" rel="stylesheet">
<style>
  :root {
    --orange: #f37122;
    --green: #9bcb3c;
    --pale-green: #cadf82;
    --logo-green: #1f8a3a;
    --ink: #1a1a1a;
    --band: #231f20;
    --paper: #ffffff;
    --stage: #161616;
  }
  * { margin: 0; padding: 0; box-sizing: border-box; }
  html, body {
    width: 1200px; height: 902px; overflow: hidden;
    background: var(--stage);
    font-family: "Open Sans", Arial, sans-serif;
  }
  .card {
    position: absolute; left: 50px; top: 138px;
    width: 1100px; height: 626px;
    background: var(--paper); overflow: hidden;
  }
  .brand {
    position: absolute; left: 46px; top: 62px;
    display: flex; align-items: center; gap: 18px;
  }
  .brand-sun {
    width: 92px; height: 92px; border-radius: 50%;
    background: var(--orange); flex: none;
  }
  .brand-text { line-height: 1.1; }
  .brand-name {
    display: block; color: var(--logo-green);
    font-size: 48px; font-weight: 600; letter-spacing: -0.5px; white-space: nowrap;
  }
  .brand-services {
    display: block; margin-top: 6px; color: var(--logo-green);
    font-size: 24px; font-weight: 400; white-space: nowrap;
  }
  .contact {
    position: absolute; right: 66px; top: 46px;
    text-align: right; color: var(--ink);
  }
  .contact-name { color: var(--green); font-size: 40px; font-weight: 600; line-height: 1.1; }
  .contact-business { color: var(--orange); font-size: 27px; line-height: 1.3; margin-bottom: 10px; }
  .contact-line {
    display: flex; justify-content: flex-end; align-items: center; gap: 10px;
    font-size: 27px; line-height: 38px;
  }
  .contact-icon { width: 26px; height: 26px; flex: none; }
  .rule-green {
    position: absolute; left: 0; top: 236px; width: 100%; height: 10px;
    background: var(--green);
  }
  .rule-dark {
    position: absolute; left: 0; width: 100%; height: 6px; background: var(--band);
  }
  .rule-dark.top { top: 252px; }
  .rule-dark.bottom { top: 522px; }
  .gallery {
    position: absolute; left: 0; top: 262px; width: 100%; height: 258px;
    display: grid; grid-template-columns: repeat(4, 1fr); gap: 5px;
  }
  .photo { height: 100%; }
  .photo.steps { background: linear-gradient(160deg, #8a7a66 0%, #6f8a45 55%, #a0846a 100%); }
  .photo.path { background: linear-gradient(150deg, #5b6a58 0%, #4f8f2e 45%, #7fc13a 100%); }
  .photo.bridge { background: linear-gradient(170deg, #9fbf70 0%, #6b5a3a 40%, #5f7a3c 70%, #6aa83a 100%); }
  .photo.garden { background: linear-gradient(160deg, #4f8a2e 0%, #7ab640 50%, #8f8a6a 100%); }
  .tagline-band {
    position: absolute; left: 0; top: 538px; width: 100%; height: 88px;
    background: var(--band); color: var(--paper);
    display: flex; align-items: center; justify-content: center;
    font-size: 28px;
  }
</style>
</head>
<body>
  <div class="card">
    <div class="brand">
      <div class="brand-sun"></div>
      <div class="brand-text">
        <span class="brand-name">Brindle Yard Care</span>
        <span class="brand-services">Mowing · Trimming · Edging · Clean up</span>
      </div>
    </div>

    <div class="contact">
      <div class="contact-name">Dorian</div>
      <div class="contact-business">Brindle Yard care</div>
      <div class="contact-line">
        <span>482-615-0273</span>
        <svg class="contact-icon" viewBox="0 0 26 26" aria-hidden="true">
          <rect width="26" height="26" fill="#f37122"/>
          <path d="M5 11 Q13 4 21 11 L19 13 L16 11 L16 9 Q13 8 10 9 L10 11 L7 13 Z" fill="#fff"/>
          <rect x="7" y="14" width="12" height="7" rx="1" fill="#fff"/>
        </svg>
      </div>
      <div class="contact-line">
        <span>tomkerl47@quillmail.net</span>
        <svg class="contact-icon" viewBox="0 0 26 26" aria-hidden="true">
          <rect width="26" height="26" fill="#f37122"/>
          <rect x="5" y="7" width="16" height="12" fill="none" stroke="#fff" stroke-width="2"/>
          <path d="M5 7 L13 14 L21 7 M5 19 L11 13 M21 19 L15 13" fill="none" stroke="#fff" stroke-width="1.6"/>
        </svg>
      </div>
    </div>

    <div class="rule-green"></div>
    <div class="rule-dark top"></div>

    <div class="gallery">
      <div class="photo steps" role="img" aria-label="Stone patio steps with a retaining wall and shrubs"></div>
      <div class="photo path" role="img" aria-label="Curving paver walkway beside a freshly mowed lawn"></div>
      <div class="photo bridge" role="img" aria-label="Garden pond with an arched wooden bridge and red maple"></div>
      <div class="photo garden" role="img" aria-label="Cottage garden with stepping stone path and bench"></div>
    </div>

    <div class="rule-dark bottom"></div>

    <div class="tagline-band">100% satisfaction guarantee. Fast, Friendly, quality service</div>
  </div>
</body>
</html>
```